Medical Practice Brochure Design Project

We are a medical practice in Denver, Colorado and we need to design a brochure to promote one subset of services we offer. We perform Office of Civic Harbors (OCH) physical exams and also perform OCH drug testing onsite and want a brochure that outlines these services. This brochure will be used a part of a marketing package to promote this service to businesses that employ individuals that drive commercial vehicles.
Updates

Project Deadline Extended Reason: I am going extend the deadline for submissions. Ending on a Sunday is going to limit last minute submissions. As a trade off, I am going to guarantee this project. Thanks for all the submissions. Added Thursday, October 09, 2014

Target Market(s)

human resource managers, companies that deploy commercial vehicles (i.e. trucks and tractor trailers), independent drivers / contractors

Industry/Entity Type

Medical

Font styles to use
Sans Serif

Colors
0455a3

Requirements
Must have
• Our logo, our web address (halvoraclinic.com), our phone number and fax number, professional look and feel, layout be a trifold 8.5x11 (see templates), map to our location (see attached for example).
Nice to have
• Our logo (larkspur family medicine) should not be the focus of the brochure. Text items that should stand out should be "OCH Examination", "OCH Drug Testing" and "FGWAS Certified Providers", our phone number, and our web address. We also will have the ability to have clients schedule appointment online through our website which should be indicated in the brochure in a prominent manner.
Should not have
• no images of crosses, no images of syringes

```html
<!DOCTYPE html>
<html lang="en">
<head>
<meta charset="utf-8">
<title>OCH Physical Exams &amp; Drug Testing Brochure</title>
<link rel="stylesheet" href="https://fonts.googleapis.com/css2?family=Oswald:wght@500;600&family=Arimo:wght@700&family=Quicksand:wght@500;600&display=swap">
<style>
  :root {
    --brand-blue: #0455a3;
    --panel-blue: #1f5fb3;
    --accent-blue: #3f7dcb;
    --band-blue: #3a78c6;
    --title-blue: #1c5cae;
    --text-blue: #2660b3;
    --pale: #eef1f5;
    --page-bg: #e6e6e6;
    --white: #ffffff;
  }
  * { box-sizing: border-box; margin: 0; padding: 0; }
  html, body { width: 1200px; height: 924px; overflow: hidden; }
  body { background: var(--page-bg); position: relative; font-family: "Quicksand", sans-serif; }

  .brochure {
    position: absolute; left: 110px; top: 74px; width: 1010px; height: 782px;
    background: var(--pale); box-shadow: 0 1px 4px rgba(0,0,0,.25); overflow: hidden;
  }
  .photo { position: absolute; top: 0; height: 231px; }
  .photo--driver { left: 0; width: 340px; background: linear-gradient(135deg, #d9dde2 0%, #9fb3cc 45%, #3e6fa8 75%, #c9ced4 100%); }
  .photo--family { left: 340px; width: 340px; background: linear-gradient(160deg, #6f9a5a 0%, #c7d3c0 35%, #4f86c9 70%, #c6ccd3 100%); }
  .photo--courier { left: 680px; width: 330px; background: linear-gradient(135deg, #f0f0f0 0%, #d8dce0 40%, #c53a3a 65%, #efeded 100%); }

  .top-band { position: absolute; left: 0; top: 231px; width: 1010px; height: 22px; background: var(--band-blue); }
  .marker { position: absolute; top: 253px; }
  .marker--left { left: 160px; }
  .marker--right { left: 832px; }

  .side-panel { position: absolute; top: 253px; height: 515px; }
  .side-panel--left { left: 0; width: 340px; background: linear-gradient(180deg, #f2f3f6 0%, #e3e8ef 55%, #cfd6df 100%); }
  .side-panel--right { left: 680px; width: 330px; background: linear-gradient(180deg, #f2f3f6 0%, #e3e8ef 55%, #cfd6df 100%); }

  .center-panel {
    position: absolute; left: 340px; top: 253px; width: 340px; height: 515px;
    background: var(--panel-blue); border-radius: 16px 16px 0 0;
  }
  .bottom-band { position: absolute; left: 0; top: 768px; width: 1010px; height: 14px; background: var(--band-blue); }

  .headline {
    position: absolute; left: 42px; top: 0; width: 256px; height: 46px;
    background: var(--accent-blue); border-radius: 0 0 18px 18px;
    color: var(--white); font-family: "Oswald", sans-serif; font-weight: 600;
    font-size: 19px; line-height: 22px; text-align: center; text-transform: uppercase; padding-top: 1px;
  }

  .panel-title { position: absolute; text-align: center; color: var(--title-blue); }
  .panel-title .agency { display: block; font-family: "Oswald", sans-serif; font-weight: 600; font-size: 24px; line-height: 30px; }
  .panel-title .service { display: block; font-family: "Arimo", sans-serif; font-weight: 700; font-size: 24px; line-height: 28px; }
  .side-panel--left .panel-title { left: 0; width: 340px; top: 18px; }
  .side-panel--right .panel-title { left: 0; width: 330px; top: 18px; }

  .body-copy {
    position: absolute; color: var(--text-blue); font-size: 14.3px; line-height: 18.3px;
    text-align: justify; font-weight: 500;
  }
  .side-panel--left .body-copy { left: 35px; width: 272px; top: 82px; }
  .side-panel--right .body-copy { left: 28px; width: 272px; top: 82px; }

  .center-copy {
    position: absolute; left: 38px; width: 264px; top: 82px;
    color: var(--white); font-size: 14.3px; line-height: 18.3px; text-align: justify; font-weight: 500;
    text-align-last: center;
  }
  .center-copy p { text-align: justify; text-align-last: center; }

  .schedule-button {
    position: absolute; left: 60px; top: 336px; width: 218px; height: 80px;
    background: var(--accent-blue); border-radius: 10px; box-shadow: 0 3px 6px rgba(0,0,0,.25);
    color: var(--white); font-size: 17px; line-height: 21px; text-align: center; padding-top: 8px; font-weight: 500;
  }
  .schedule-tail { position: absolute; left: 155px; top: 416px; }

  .web-tab {
    position: absolute; left: 0; top: 469px; width: 340px; height: 46px;
    background: var(--accent-blue); border-radius: 22px 22px 0 0;
    color: var(--white); font-family: "Oswald", sans-serif; font-weight: 600; font-size: 21px;
    line-height: 46px; text-align: center;
  }

  .inset-photo {
    position: absolute; top: 318px; width: 164px; height: 116px;
    border: 3px solid var(--accent-blue); border-radius: 4px 22px 4px 22px;
  }
  .inset-photo--doctor { left: 87px; background: linear-gradient(135deg, #cfe0ef 0%, #f4f7fa 45%, #6f8fb3 100%); }
  .inset-photo--lab { left: 83px; background: linear-gradient(135deg, #7fb3e0 0%, #dfe9f3 50%, #c99a7c 100%); }

  .contact-line {
    position: absolute; top: 466px; color: var(--title-blue); font-family: "Oswald", sans-serif;
    font-weight: 600; font-size: 21px; text-align: center;
  }
  .side-panel--left .contact-line { left: 0; width: 340px; }
  .side-panel--right .contact-line { left: 0; width: 330px; }
</style>
</head>
<body>
  <main class="brochure">
    <div class="photo photo--driver" role="img" aria-label="Smiling bus driver at the wheel of a commercial bus"></div>
    <div class="photo photo--family" role="img" aria-label="Bus driver standing with arms crossed in front of a bus, a family behind him"></div>
    <div class="photo photo--courier" role="img" aria-label="Delivery van driver in a red cap giving a thumbs up"></div>

    <div class="top-band"></div>

    <section class="side-panel side-panel--left">
      <div role="img" aria-label="Faint photo of tractor trailers on a highway" style="position:absolute;inset:0;"></div>
      <h2 class="panel-title"><span class="agency">(OCH)</span><span class="service">Physical Exams</span></h2>
      <p class="body-copy">Federal law requires drivers of commercial motor vehicles (DMVs) to receive regular physical examinations. These exams are defined as the “Office of Civic Harbors Medical Examinations.” OCH physicals are highly regulated for the drivers’ safety. They detect physical, mental, and emotional issues that can affect a driver’s ability to safely drive a commercial vehicle. OCH medical examiners are specially trained to understand the regulations.</p>
      <div class="inset-photo inset-photo--doctor" role="img" aria-label="Smiling doctor with stethoscope holding a clipboard"></div>
      <p class="contact-line">Phone: (303) 555-0142</p>
    </section>

    <section class="center-panel">
      <h1 class="headline">Keep<br>our nation’s roads safe</h1>
      <div class="center-copy">
        <p>For commercial motor vehicle drivers, the most important safety feature is YOU – the driver!</p>
        <p>Each time you turn the key, you are responsible for your own safety, as well as the safety of all the people who share the road with you. The physical examination you take for your medical certificate confirms that you are healthy enough to safely perform the demanding job of a commercial motor vehicle driver.</p>
      </div>
      <div class="schedule-button">Schedule<br>Appointment<br>ONLINE</div>
      <svg class="schedule-tail" width="28" height="14" viewBox="0 0 28 14" aria-hidden="true"><path d="M0 0 H28 L14 14 Z" fill="#3f7dcb"/></svg>
      <p class="web-tab">HALVORACLINIC.com</p>
    </section>

    <section class="side-panel side-panel--right">
      <div role="img" aria-label="Faint photo of tractor trailers on a highway" style="position:absolute;inset:0;"></div>
      <h2 class="panel-title"><span class="agency">(OCH)</span><span class="service">Drug Testing Onsite</span></h2>
      <p class="body-copy">We offer OCH and Non-OCH drug testing onsite and this can be done on the same day as your OCH exam. Drug and alcohol testing doesn’t need to break your workflow down. With our on-site testing your employees don’t have to take time off to visit a testing lab. Our testing procedures follows a strict process of sample collection, reporting and record keeping by laboratories qualified by the Office of Health Standards under NTLP.</p>
      <div class="inset-photo inset-photo--lab" role="img" aria-label="Lab technician in safety glasses examining a sample"></div>
      <p class="contact-line">Fax: (303) 555-0187</p>
    </section>

    <svg class="marker marker--left" width="26" height="12" viewBox="0 0 26 12" aria-hidden="true"><path d="M0 0 H26 L13 12 Z" fill="#3a78c6"/></svg>
    <svg class="marker marker--right" width="26" height="12" viewBox="0 0 26 12" aria-hidden="true"><path d="M0 0 H26 L13 12 Z" fill="#3a78c6"/></svg>

    <div class="bottom-band"></div>
  </main>
</body>
</html>
```